Business Cards for a small business advisory (business services)

Professional look. Same as would apply for a lawyer, accountant, or other financial services professional. Please use the logo colors

Target Market(s)

small business owners

Industry/Entity Type

Financial Servics

Contact Information for Business Card

Name: Gavin L. Whitmore, CAIA / Title: Business Advisor / Office #: (718) 294-7716 / Mobile #: (917) 382-5047 / Email: g.whitmore@clearfieldventurepartners.example / Web: www.clearfieldventurepartners.example

Font styles to use
Sans Serif

```html
<!DOCTYPE html>
<html lang="en">
<head>
<meta charset="utf-8">
<title>Clearfield Venture Partners – Business Cards</title>
<link rel="stylesheet" href="https://fonts.googleapis.com/css2?family=Montserrat:wght@600;700&family=Open+Sans:wght@400;700&display=swap">
<style>
  :root {
    --navy: #0d2358;
    --green: #6ab023;
    --paper: #f1f1f0;
    --backdrop: #d6d6d6;
    --ink: #1b1b1b;
  }
  * { margin: 0; padding: 0; box-sizing: border-box; }
  html, body { width: 1200px; height: 1051px; overflow: hidden; background: var(--backdrop); }
  .sheet {
    position: relative; width: 1200px; height: 1051px;
    display: flex; flex-direction: column; align-items: center; justify-content: center; gap: 50px;
  }
  .card {
    position: relative; width: 770px; height: 440px; background: var(--paper);
    border-bottom: 8px solid var(--green); overflow: hidden;
    box-shadow: 0 6px 18px rgba(0,0,0,0.12);
  }
  .wordmark { position: absolute; display: flex; align-items: flex-start; gap: 14px; }
  .wordmark-dot { width: 40px; height: 40px; border-radius: 50%; background: var(--navy); margin-top: 6px; flex: none; }
  .wordmark-text { display: flex; flex-direction: column; }
  .brand-name {
    font-family: "Montserrat", sans-serif; font-weight: 700; color: var(--navy);
    font-size: 44px; line-height: 1; letter-spacing: -0.3px; max-width: 420px;
  }
  .brand-tagline {
    font-family: "Montserrat", sans-serif; font-weight: 700; color: var(--green);
    font-size: 11px; letter-spacing: 0.5px; text-transform: uppercase; margin-top: 8px;
  }
  .card-front .wordmark { top: 44px; right: 60px; }
  .card-back .wordmark { top: 150px; right: 80px; }
  .edge-tab { position: absolute; right: 0; top: 250px; width: 22px; height: 44px; background: var(--green); }
  .contact {
    position: absolute; right: 60px; top: 200px; text-align: right;
    font-family: "Open Sans", sans-serif; color: var(--ink);
  }
  .person-name { font-family: "Montserrat", sans-serif; font-weight: 700; font-size: 30px; color: var(--navy); }
  .person-title { font-size: 19px; margin-top: 2px; }
  .contact-list { list-style: none; margin-top: 22px; font-size: 17px; line-height: 1.45; }
  .contact-list li { display: flex; justify-content: flex-end; align-items: center; gap: 10px; }
  .contact-list svg { width: 15px; height: 15px; fill: var(--navy); flex: none; }
</style>
</head>
<body>
<main class="sheet">
  <section class="card card-front" aria-label="Business card front">
    <div class="wordmark">
      <span class="wordmark-dot"></span>
      <div class="wordmark-text">
        <span class="brand-name">Clearfield Venture Partners</span>
        <span class="brand-tagline">Steady counsel for owners planning their next business move</span>
      </div>
    </div>
    <div class="edge-tab"></div>
    <div class="contact">
      <p class="person-name">Gavin L. Whitmore, CAIA</p>
      <p class="person-title">Business Advisor</p>
      <ul class="contact-list">
        <li>(718) 294-7716
          <svg viewBox="0 0 16 16" aria-hidden="true"><path d="M3.5 1 6 4 4.6 5.6a9 9 0 0 0 5.8 5.8L12 10l3 2.5-1.5 2.4C8 15 1 8 1.1 2.5z"/></svg></li>
        <li>(917) 382-5047
          <svg viewBox="0 0 16 16" aria-hidden="true"><path d="M4 0h8a1 1 0 0 1 1 1v14a1 1 0 0 1-1 1H4a1 1 0 0 1-1-1V1a1 1 0 0 1 1-1zm1 2v10h6V2zm3 11a1 1 0 1 0 0 2 1 1 0 0 0 0-2z"/></svg></li>
        <li>g.whitmore@clearfieldventurepartners.example
          <svg viewBox="0 0 16 16" aria-hidden="true"><path d="M1 3h14v10H1zm1.5 1.2v.4L8 9l5.5-4.4v-.4zM2.5 6v5.8h11V6L8 10.4z"/></svg></li>
        <li>www.clearfieldventurepartners.example
          <svg viewBox="0 0 16 16" aria-hidden="true"><circle cx="8" cy="8" r="7"/></svg></li>
      </ul>
    </div>
  </section>

  <section class="card card-back" aria-label="Business card back">
    <div class="wordmark">
      <span class="wordmark-dot"></span>
      <div class="wordmark-text">
        <span class="brand-name">Clearfield Venture Partners</span>
        <span class="brand-tagline">Steady counsel for owners planning their next business move</span>
      </div>
    </div>
  </section>
</main>
</body>
</html>
```